RK Cooling (logo) - Celebrating 55 Years Servicing the Chicago Suburbs. Summer is Almost Here! Make sure your system is running properly and efficiently. The industry standard recommends an A/C Clean & Check once a year.
A/C Clean & Check
Regular Preventive Maintenance Can:
-Help Prolong the Life of your Equipment
-Help Lower Your Monthly Energy Costs
-Save Costs on Future Repairs

Mention this Postcard and Take $10.00 Off
Call (555) 384-9120 I Address: 718 Birchwood Ave. Marvale, IL
_______________________________________________
BACK SIDE:
Proudly Serving Chicagoland Area Since 1961- We Also Service and Sell:
-Coastline Prime Equipment.
-Brightvane Air Cleaners & Humidifier Systems.
-Hot Water Heaters, Boilers, and Digital Thermostats.
-Residential and Commercial Fabrication. Custom Welding.

Schedule Your Spring Clean & Check Today
Phone: (555) 384-9120
Mail: rkcooling@mailnest.example
Website: www.rkcoolingair.example

I had pixel guild make a Fall Clean and Check (for furnaces) in September of 2015. Feel free too look back for ideas. The postcard needs to be creative and not the same as the fall one! Added Tuesday, March 29, 2016

Target Market(s)

HVAC Industry, Residential

Industry/Entity Type

Air Conditioning

Colors
0255a3
f6faec

Requirements
Must have
• The following text in the project description. Feel free to add more.
Nice to have
• One small picture or clipart on the front. Maybe a picture of something summery or an air conditioner.
Should not have
• No spelling mistakes. Nothing too basic.

```html
<!DOCTYPE html>
<html lang="en">
<head>
<meta charset="utf-8">
<title>RK Cooling – Spring A/C Clean &amp; Check Postcard</title>
<link rel="stylesheet" href="https://fonts.googleapis.com/css2?family=Questrial&family=Oswald:wght@400;500;600&display=swap">
<style>
  :root {
    --brand-blue: #0255a3;
    --deep-blue: #1d4fa0;
    --navy: #1e2a78;
    --sky-blue: #2b8fd6;
    --orange: #f7931e;
    --orange-dark: #ee7b12;
    --alert-red: #e0312b;
    --cream: #f6faec;
    --ink: #2a2a2a;
    --paper: #ffffff;
    --paper-shade: #ececec;
    --backdrop: #e4e4e4;
  }
  * { box-sizing: border-box; margin: 0; padding: 0; }
  html, body { width: 900px; height: 1200px; overflow: hidden; }
  body {
    background: var(--backdrop);
    font-family: "Questrial", "Century Gothic", sans-serif;
    color: var(--ink);
    position: relative;
  }
  .postcard {
    position: absolute;
    width: 704px;
    height: 546px;
    background: linear-gradient(135deg, var(--paper) 0%, #f7f7f7 55%, var(--paper-shade) 100%);
    overflow: hidden;
    box-shadow: 0 2px 6px rgba(0,0,0,.18);
  }
  .postcard--front { left: 98px; top: 33px; }
  .postcard--back { left: 102px; top: 620px; }
  .card-shapes { position: absolute; inset: 0; }

  /* ---------- front ---------- */
  .brand-name {
    position: absolute; left: 112px; top: 50px;
    display: flex; align-items: center; gap: 8px;
    font-size: 32px; color: var(--navy); letter-spacing: .5px;
  }
  .brand-name .brand-dot { width: 14px; height: 14px; border-radius: 50%; background: var(--navy); }

  .headline {
    position: absolute; left: 40px; top: 160px;
    font-size: 36px; color: var(--brand-blue); font-weight: 400; letter-spacing: .5px;
  }
  .subhead {
    position: absolute; left: 40px; top: 208px;
    font-size: 19px; color: var(--brand-blue);
  }
  .benefits {
    position: absolute; left: 40px; top: 244px; list-style: none;
    font-size: 16px; line-height: 26px;
  }
  .tick-list li { display: flex; align-items: flex-start; gap: 8px; }
  .tick-list svg { flex: none; margin-top: 5px; }
  .intro {
    position: absolute; left: 40px; top: 328px; width: 305px;
    font-size: 15px; line-height: 20px;
  }
  .intro-highlight {
    position: absolute; left: 40px; top: 386px;
    font-size: 18px; color: var(--brand-blue);
  }

  .anniversary {
    position: absolute; left: 467px; top: 0; width: 200px; height: 185px;
  }
  .service-area {
    position: absolute; left: 410px; top: 197px; width: 290px; text-align: center;
    font-family: "Oswald", sans-serif; font-weight: 500; font-size: 15px; color: var(--brand-blue);
  }
  .rating-box {
    position: absolute; left: 412px; top: 225px; width: 280px; height: 47px;
    background: var(--orange-dark); border: 2px solid var(--paper); outline: 1px solid var(--orange-dark);
    color: var(--paper); text-align: center;
    font-family: "Oswald", sans-serif; font-weight: 500; font-size: 14px; line-height: 19px; padding-top: 3px;
  }
  .rating-box .stars { font-size: 8px; letter-spacing: 1px; vertical-align: middle; }

  .unit-illustration {
    position: absolute; left: 412px; top: 297px; width: 270px; height: 212px;
    background: linear-gradient(160deg, #f3f3f3 0%, #c9cbcc 55%, #8d9092 100%);
    border-radius: 6px;
  }

  .discount-seal { position: absolute; left: 40px; top: 424px; width: 136px; height: 120px; }

  .call-block { position: absolute; left: 192px; top: 444px; }
  .call-number {
    display: flex; align-items: center; gap: 8px;
    font-size: 22px; color: var(--brand-blue); font-weight: 400;
  }
  .call-action {
    margin-top: 6px; font-family: "Oswald", sans-serif; font-weight: 600;
    font-size: 17px; color: var(--ink); letter-spacing: .5px;
  }
  .address {
    position: absolute; left: 434px; top: 518px;
    display: flex; align-items: center; gap: 8px;
    font-size: 17px; color: var(--paper);
  }

  /* ---------- back ---------- */
  .stamp-box {
    position: absolute; left: 601px; top: 28px; width: 75px; height: 82px;
    border: 1px solid #333; background: var(--paper);
  }
  .since-heading {
    position: absolute; left: 28px; top: 24px;
    color: var(--brand-blue); line-height: 27px;
  }
  .since-heading .line-lg { font-size: 25px; display: block; }
  .since-heading .line-md { font-size: 21px; display: block; }
  .offer-title {
    position: absolute; left: 28px; top: 115px; font-size: 18px;
  }
  .product-list {
    position: absolute; left: 28px; top: 145px; width: 360px; list-style: none;
    font-size: 16px; line-height: 22px;
  }
  .product-list li { margin-bottom: 4px; }

  .schedule-panel {
    position: absolute; left: 0; top: 325px; width: 426px; height: 127px;
    background: linear-gradient(90deg, var(--brand-blue) 0%, var(--sky-blue) 100%);
    color: var(--paper); padding: 10px 0 0 27px;
  }
  .schedule-title {
    font-family: "Oswald", sans-serif; font-weight: 400; font-size: 24px; line-height: 30px;
  }
  .contact-list { list-style: none; margin-top: 2px; font-size: 17px; line-height: 27px; }
  .contact-list li { display: flex; align-items: center; gap: 10px; }
  .fine-print {
    position: absolute; left: 30px; top: 458px; font-size: 8px; color: #444;
  }
</style>
</head>
<body>

<!-- FRONT -->
<section class="postcard postcard--front" aria-label="Postcard front">
  <svg class="card-shapes" width="704" height="546" viewBox="0 0 704 546" aria-hidden="true">
    <!-- top chevron -->
    <path d="M0,62 L222,142 L470,66 L470,70 L222,150 L0,70 Z" fill="var(--orange)"/>
    <path d="M0,40 L222,130 L470,60 L222,140 L0,60 Z" fill="var(--brand-blue)"/>
    <!-- lower bands -->
    <path d="M0,494 Q80,500 150,512 L196,546 L0,546 Z" fill="var(--orange)"/>
    <path d="M0,504 Q70,510 136,522 L176,546 L0,546 Z" fill="var(--brand-blue)"/>
    <path d="M300,546 Q500,470 704,372 L704,546 Z" fill="var(--orange)"/>
    <path d="M330,546 Q520,480 704,392 L704,546 Z" fill="var(--brand-blue)"/>
  </svg>

  <div class="brand-name"><span class="brand-dot"></span>RK COOLING</div>

  <svg class="anniversary" viewBox="0 0 200 185" role="img" aria-label="Celebrating 55 years badge">
    <circle cx="92" cy="92" r="72" fill="var(--orange)"/>
    <circle cx="92" cy="92" r="58" fill="none" stroke="var(--paper)" stroke-width="3" stroke-dasharray="1 9" stroke-linecap="round"/>
    <circle cx="92" cy="92" r="52" fill="var(--orange-dark)"/>
    <text x="92" y="118" text-anchor="middle" font-family="Oswald, sans-serif" font-weight="600" font-size="58" fill="var(--paper)">55</text>
    <text x="92" y="140" text-anchor="middle" font-family="Oswald, sans-serif" font-size="16" fill="var(--paper)">YEARS</text>
    <text x="92" y="62" text-anchor="middle" font-size="10" fill="var(--paper)">★ ★ ★</text>
    <path d="M0,152 L16,152 L10,164 L16,176 L0,176 Z" fill="var(--brand-blue)"/>
    <path d="M184,152 L200,152 L200,176 L184,176 L190,164 Z" fill="var(--brand-blue)"/>
    <rect x="12" y="146" width="170" height="36" fill="var(--brand-blue)"/>
    <rect x="16" y="150" width="162" height="28" fill="none" stroke="var(--paper)" stroke-width="1.5"/>
    <text x="97" y="173" text-anchor="middle" font-family="Oswald, sans-serif" font-size="23" fill="var(--paper)">CELEBRATING</text>
  </svg>

  <p class="service-area">SERVICING THE CHICAGO SUBURBS</p>
  <p class="rating-box">RATED 5 STARS - BEST AND MOST EXPERIENCED<br>
    <span class="stars">★★★★★</span>&nbsp;&nbsp; TECHNICIANS IN TOWN &nbsp;&nbsp;<span class="stars">★★★★★</span></p>

  <div class="unit-illustration" role="img" aria-label="Illustration of air conditioning condenser units with a screwdriver and wrench"></div>

  <h1 class="headline">A/C CLEAN &amp; CHECK</h1>
  <p class="subhead">Regular Preventive Maintenance Can:</p>
  <ul class="benefits tick-list">
    <li><svg width="16" height="14" viewBox="0 0 16 14"><path d="M1,7 L6,12 L15,1" fill="none" stroke="var(--orange)" stroke-width="2.6"/></svg>Help Prolong the Life of your Equipment</li>
    <li><svg width="16" height="14" viewBox="0 0 16 14"><path d="M1,7 L6,12 L15,1" fill="none" stroke="var(--orange)" stroke-width="2.6"/></svg>Help Lower Your Monthly Energy Costs</li>
    <li><svg width="16" height="14" viewBox="0 0 16 14"><path d="M1,7 L6,12 L15,1" fill="none" stroke="var(--orange)" stroke-width="2.6"/></svg>Save Costs on Future Repairs</li>
  </ul>
  <p class="intro">Summer is Almost Here! Make sure your system is running properly and efficiently. The industry standard recommends an</p>
  <p class="intro-highlight">A/C Clean &amp; Check Once a Year.</p>

  <svg class="discount-seal" viewBox="0 0 136 120" role="img" aria-label="Mention this postcard and take $10.00 off">
    <defs><path id="seal-arc" d="M16.8,73 A52,52 0 0 1 119.2,55"/></defs>
    <circle cx="68" cy="64" r="46" fill="var(--paper)" stroke="var(--deep-blue)" stroke-width="5"/>
    <text font-family="Oswald, sans-serif" font-size="11" fill="var(--orange-dark)" letter-spacing=".4" text-anchor="middle"><textPath href="#seal-arc" startOffset="50%">MENTION THIS POSTCARD AND</textPath></text>
    <text x="68" y="60" text-anchor="middle" font-family="Oswald, sans-serif" font-weight="600" font-size="19" fill="var(--alert-red)">TAKE</text>
    <rect x="8" y="65" width="120" height="26" fill="var(--orange)"/>
    <text x="68" y="86" text-anchor="middle" font-family="Oswald, sans-serif" font-weight="600" font-size="21" fill="var(--paper)">$10.00</text>
    <text x="68" y="109" text-anchor="middle" font-family="Oswald, sans-serif" font-weight="600" font-size="18" fill="var(--alert-red)">OFF</text>
  </svg>

  <div class="call-block">
    <p class="call-number">
      <svg width="24" height="24" viewBox="0 0 24 24" aria-hidden="true"><circle cx="12" cy="12" r="10.5" fill="none" stroke="var(--orange)" stroke-width="2"/><path d="M8.5,7 L10.3,7 L11,9.6 L9.8,10.6 Q11,13 13.4,14.2 L14.4,13 L17,13.7 L17,15.5 Q16.5,16.8 15,16.8 Q9,16 7.2,9 Q7.2,7.5 8.5,7 Z" fill="var(--orange)"/></svg>
      (555) 384-9120
    </p>
    <p class="call-action">CALL NOW</p>
  </div>

  <p class="address">
    <svg width="14" height="20" viewBox="0 0 14 20" aria-hidden="true"><path d="M7,1 A6,6 0 0 1 13,7 C13,11 7,17 7,17 C7,17 1,11 1,7 A6,6 0 0 1 7,1 Z" fill="none" stroke="var(--paper)" stroke-width="1.6"/><circle cx="7" cy="7" r="2" fill="var(--paper)"/><path d="M2,19 H12" stroke="var(--paper)" stroke-width="1.6"/></svg>
    718 Birchwood Ave. Marvale, IL
  </p>
</section>

<!-- BACK -->
<section class="postcard postcard--back" aria-label="Postcard back">
  <svg class="card-shapes" width="704" height="546" viewBox="0 0 704 546" aria-hidden="true">
    <rect width="704" height="546" fill="var(--paper)"/>
    <path d="M0,0 L280,0 Q420,150 400,330 L400,546 L0,546 Z" fill="#f4f4f4"/>
    <path d="M310,0 Q440,180 410,360 Q395,470 270,546 L290,546 Q420,470 432,360 Q462,180 336,0 Z" fill="var(--orange)"/>
    <path d="M270,0 Q420,170 395,340 Q380,460 250,546 L268,546 Q404,460 416,340 Q440,170 308,0 Z" fill="var(--brand-blue)"/>
  </svg>

  <div class="stamp-box" aria-label="Stamp area"></div>

  <h2 class="since-heading">
    <span class="line-lg">PROUDLY SERVING</span>
    <span class="line-md">CHICAGOLAND AREA</span>
    <span class="line-md">SINCE 1961-</span>
  </h2>
  <p class="offer-title">We Also Service and Sell:</p>
  <ul class="product-list tick-list">
    <li><svg width="16" height="14" viewBox="0 0 16 14"><path d="M1,7 L6,12 L15,1" fill="none" stroke="var(--orange)" stroke-width="2.6"/></svg><span>Coastline Prime Equipment.</span></li>
    <li><svg width="16" height="14" viewBox="0 0 16 14"><path d="M1,7 L6,12 L15,1" fill="none" stroke="var(--orange)" stroke-width="2.6"/></svg><span>Brightvane Air Cleaners &amp;<br>Humidifier Systems.</span></li>
    <li><svg width="16" height="14" viewBox="0 0 16 14"><path d="M1,7 L6,12 L15,1" fill="none" stroke="var(--orange)" stroke-width="2.6"/></svg><span>Hot Water Heaters, Boilers, and<br>Digital Thermostats.</span></li>
    <li><svg width="16" height="14" viewBox="0 0 16 14"><path d="M1,7 L6,12 L15,1" fill="none" stroke="var(--orange)" stroke-width="2.6"/></svg><span>Residential and Commercial Fabrication.<br>Custom Welding.</span></li>
  </ul>

  <div class="schedule-panel">
    <p class="schedule-title">Schedule Your Spring Clean &amp; Check Today</p>
    <ul class="contact-list">
      <li><svg width="16" height="16" viewBox="0 0 24 24" aria-hidden="true"><circle cx="12" cy="12" r="10.5" fill="none" stroke="var(--paper)" stroke-width="2"/><path d="M8.5,7 L10.3,7 L11,9.6 L9.8,10.6 Q11,13 13.4,14.2 L14.4,13 L17,13.7 L17,15.5 Q16.5,16.8 15,16.8 Q9,16 7.2,9 Q7.2,7.5 8.5,7 Z" fill="var(--paper)"/></svg>(555) 384-9120</li>
      <li><svg width="16" height="12" viewBox="0 0 16 12" aria-hidden="true"><rect x=".7" y=".7" width="14.6" height="10.6" fill="none" stroke="var(--paper)" stroke-width="1.3"/><path d="M1,1 L8,7 L15,1" fill="none" stroke="var(--paper)" stroke-width="1.3"/></svg>rkcooling@mailnest.example</li>
      <li><svg width="16" height="16" viewBox="0 0 16 16" aria-hidden="true"><g fill="none" stroke="var(--paper)" stroke-width="1.3"><circle cx="8" cy="8" r="7"/><ellipse cx="8" cy="8" rx="3" ry="7"/><path d="M1,8 H15 M2,4.5 H14 M2,11.5 H14"/></g></svg>www.rkcoolingair.example</li>
    </ul>
  </div>
  <p class="fine-print">*discounts not valid for maintenance agreement. Other restrictions may apply</p>
</section>

</body>
</html>
```